Manuka honey wholesales and export company needs a website

We are a Manuka honey Wholesale and export company based in New Zealand and needing a website to attract new clients.
We produce one of the worlds best honeys so we need a clean, modern look that lets everybody know that we can supply our product around the world.
We source only the finest Manuka honey from some of the most remote parts of New Zealand and send it around the world for everyone to enjoy.
We need a website that will allow people to inquire about export or bulk purchasing as well as a buying tab with pricing but one that we can add photos to as our product labels are not complete yet.
We also support and supply local farmers markets and a page dedicated to this would be good with details on when and where they are.

Here are links to other manuka honey websites to get an idea
http://www.hivelarkfields.co.nz/
http://www.pellora.co.nz/key-ingredients/manuka-honey/nz100008?gclid=Xq7PLmRtYvBNsKdWoEjZaHuFcGiTeLpOyNbRkVwQmXsDaJzUoKiHnCtFgPlEbYrAqMdSvZuWxTeNoGjHkLrPfIsBaCqZyDm

Target Market(s)

The general public, retail shops and exporters

Industry/Entity Type

Health And Wellness

Number of Pages Required

5+ page

Font styles to use
Serif

Requirements
Must have
• 1. A page and contact details for Export and wholesale inquiries
• Desmond Harlow
• Export manager
• +64 21 438 190
• dkharlow@pelmail.co.nz
• 2. Page for the farmers market we supply our product to.
• Details....
• Contact: Neil Forbes
• +64 21 067 4183
• tideflowernz@mailpost.com
• MARKET INFORMATION
• Quaywell Market
• The market operates year round and is located on Ferndell Square.*
• http://quaywell.org/sol-verde-market/
• Saturday 8am-1pm
• Sunday 9am-1pm
• Ashgrove Hamlet Market
• http://www.ashgrovegrowersmarket.co.nz/
• 64 Paddock Ln, Oakhurst, Auckland 2469, New Zealand
• Market is held each Sunday from 8:30am-1pm.
• 3. An information page on manuka honey....i will attach info but most of the info you can find on other manuka honey websites..
• Health benefits..
• There are two main components of Manuka honey which give it many health benefits:
• - Hydrogen peroxide, a naturally antibiotic found in Manuka honey.
• - Methylglyoxal (MG). A powerful antibiotic compound found in large quantities in Manuka honey.
• What is MGO?
• The MGO indicates the amount of Methylglyoxal in the honey. The higher the MGO rating the more antibacterial properties are in the honey.
• Proven health Benefits of Active Manuka are....
• Aiding in the treatment of:
• - -Common Cold and Flu
• - -sore throats
• - -cuts and abrasions
• - -Reduce hair loss and scalp problems
• - -treating fungal infections
• - -Burns
• - -ulsers
• - -strengthening the immune system
• 4. A product page with a range of our products with a link yo by direct from us
• The details for this page will need to be added later as we are still doing our range!
Nice to have
• Feel free to make up a mission statement or whatever inspires you to make this a great website.
Should not have
• Go crazy please! I trust you will come up with something amazing :)

```html
<!DOCTYPE html>
<html lang="en">
<head>
<meta charset="utf-8">
<title>Tideflower Honey NZ Limited</title>
<link rel="stylesheet" href="https://fonts.googleapis.com/css2?family=Libre+Baskerville:wght@700&family=Open+Sans:ital,wght@0,400;0,600;0,700;1,600&family=Playfair+Display:ital,wght@1,700&family=Quicksand:wght@500&display=swap">
<style>
:root{
  --honey:#f0d000;
  --gold:#e7b821;
  --dark:#3a3a3a;
  --charcoal:#333333;
  --footer:#2a2a2a;
  --ink:#222222;
  --muted:#8a8a8a;
  --white:#ffffff;
}
*{margin:0;padding:0;box-sizing:border-box}
html,body{width:1200px;height:2462px;overflow:hidden}
body{position:relative;font-family:"Open Sans",Arial,sans-serif;background:var(--white);color:var(--ink)}
.abs{position:absolute}

/* header */
.site-header{position:absolute;left:0;top:0;width:1200px;height:94px;background:var(--dark)}
.brand{position:absolute;left:85px;top:56px;display:flex;align-items:center;gap:8px;color:var(--honey);font-size:19px;font-weight:400}
.brand-dot{width:14px;height:14px;border-radius:50%;background:var(--honey)}
.cart{position:absolute;right:34px;top:18px;color:var(--white);font-size:11px;display:flex;align-items:center;gap:10px}
.main-nav{position:absolute;top:53px;left:481px;display:flex;height:36px}
.main-nav a{color:var(--white);text-decoration:none;font-size:13px;line-height:36px;padding:0 19px}
.main-nav a.active{background:var(--honey);color:var(--ink);width:80px;text-align:center;padding:0}
.main-nav a.active+a{margin-left:2px}

/* hero */
.hero{position:absolute;left:0;top:94px;width:1200px;height:678px;background:linear-gradient(100deg,#c98a1f 0%,#e9c36a 25%,#f2ead8 50%,#e5c98f 70%,#e0a52c 100%)}
.hero-shade{position:absolute;inset:0;background:rgba(0,0,0,.15)}
.hero-mark{position:absolute;left:555px;top:240px;width:90px;height:90px;border-radius:50%;background:var(--honey)}
.hero-title{position:absolute;left:0;width:1200px;top:368px;text-align:center;font-family:"Playfair Display",Georgia,serif;font-style:italic;font-weight:700;font-size:68px;color:var(--white);text-shadow:0 2px 6px rgba(0,0,0,.35)}
.hero-title span{color:var(--honey)}
.hero-sub{position:absolute;left:0;width:1200px;top:472px;text-align:center;font-weight:700;font-size:19px;color:var(--honey);letter-spacing:.3px}
.btn-pill{position:absolute;top:629px;height:39px;width:119px;border-radius:20px;font-size:12px;font-weight:700;display:flex;align-items:center;justify-content:center;text-transform:uppercase}
.btn-pill.solid{left:474px;background:var(--honey);color:var(--ink)}
.btn-pill.outline{left:601px;border:2px solid var(--white);color:var(--white)}
.slide-arrow{position:absolute;top:336px;width:77px;height:73px;background:rgba(255,255,255,.25);display:flex;align-items:center;justify-content:center}
.slide-arrow.left{left:0}
.slide-arrow.right{right:0}

/* overview */
.overview{position:absolute;left:0;top:772px;width:1200px;height:484px;background:linear-gradient(90deg,#f4f4f4 0%,#ececec 55%,#d8d8d8 100%)}
.section-title{position:absolute;font-family:"Libre Baskerville",Georgia,serif;font-weight:700;font-size:28px;color:var(--honey);text-transform:uppercase}
.divider{position:absolute;height:1px;background:#c9c9c9}
.divider-dots{position:absolute;display:flex;gap:2px}
.divider-dots i{width:11px;height:11px;border-radius:50%;background:#5a5a5a;display:block}
.overview-sub{position:absolute;left:111px;top:950px;font-style:italic;font-weight:600;font-size:22px;color:var(--ink)}
.overview-text{position:absolute;left:107px;top:988px;width:956px;font-size:13px;line-height:24px;color:#555}
.btn-block{position:absolute;background:var(--honey);color:var(--ink);font-size:12px;font-weight:700;display:flex;align-items:center;justify-content:center;text-transform:uppercase}

/* products */
.products{position:absolute;left:0;top:1256px;width:1200px;height:640px;background:var(--gold)}
.products-card{position:absolute;left:64px;top:1308px;width:1070px;height:537px;background:var(--white)}
.product{position:absolute;top:1486px;width:197px}
.product-photo{width:197px;height:164px;border:1px solid #ddd}
.price{position:absolute;right:2px;top:0;width:34px;height:38px;background:var(--gold);color:var(--white);font-weight:700;font-size:17px;text-align:center;line-height:30px;clip-path:polygon(0 0,100% 0,100% 78%,50% 100%,0 78%)}
.product-name{font-family:"Quicksand",sans-serif;font-weight:500;font-size:21px;margin-top:14px;color:var(--ink)}
.product-desc{font-size:11px;color:var(--muted);line-height:16px}
.carousel-arrow{position:absolute;top:1570px}
.btn-dark{position:absolute;left:517px;top:1780px;width:166px;height:37px;background:var(--ink);color:var(--honey);font-size:12px;font-weight:700;display:flex;align-items:center;justify-content:center}

/* contact */
.contact{position:absolute;left:0;top:1896px;width:1200px;height:501px;background:var(--charcoal)}
.contact-intro{position:absolute;left:0;width:1200px;top:2015px;text-align:center;color:#d0d0d0;font-size:13px}
.contact-line{position:absolute;color:#d8d8d8;font-size:12px;line-height:22px}
.person-name{position:absolute;top:2172px;color:#d8d8d8;font-size:14px;text-transform:uppercase;line-height:18px}
.person-name small{display:block;font-size:10px;color:#bdbdbd}
.col-rule{position:absolute;left:547px;top:2077px;width:1px;height:287px;background:#555}
.form-badge{position:absolute;left:514px;top:2185px;width:66px;height:66px;border-radius:50%;background:var(--honey);display:flex;align-items:center;justify-content:center}
.field{position:absolute;border-bottom:1px solid #555;color:#c8c8c8;font-size:12px;padding-bottom:14px}
.btn-submit{position:absolute;left:627px;top:2311px;width:476px;height:36px;background:var(--honey);color:var(--ink);font-size:12px;font-weight:700;display:flex;align-items:center;justify-content:center}

/* footer */
.site-footer{position:absolute;left:0;top:2397px;width:1200px;height:65px;background:var(--footer)}
.copyright{position:absolute;left:98px;top:24px;color:#6a6a6a;font-size:12px}
.social{position:absolute;right:92px;top:18px;display:flex;gap:7px}
.social i{display:block;width:30px;height:30px;border-radius:50%;background:var(--honey)}
</style>
</head>
<body>

<header class="site-header">
  <div class="brand"><span class="brand-dot"></span>Tideflower Honey NZ Limited</div>
  <div class="cart">
    <svg width="16" height="14" viewBox="0 0 16 14" fill="none" stroke="#fff" stroke-width="1.4"><path d="M1 1h2.5l2 8h8l1.5-5.5H4.5"/><circle cx="6.5" cy="12" r="1.2"/><circle cx="12.5" cy="12" r="1.2"/></svg>
    YOUR CART (0)
  </div>
  <nav class="main-nav">
    <a class="active" href="#">Home</a><a href="#">About Us</a><a href="#">Process</a><a href="#">About Manuka</a><a href="#">Shop</a><a href="#">My Account</a><a href="#">Contact</a>
  </nav>
</header>

<section class="hero" role="img" aria-label="Photo of honey jars, a honey dipper, sponges and a beeswax candle">
  <div class="hero-shade"></div>
</section>
<div class="hero-mark"></div>
<div class="slide-arrow left"><svg width="30" height="50" viewBox="0 0 30 50"><path d="M26 2 4 25l22 23" fill="none" stroke="#eee" stroke-width="2"/></svg></div>
<div class="slide-arrow right"><svg width="30" height="50" viewBox="0 0 30 50"><path d="M4 2l22 23L4 48" fill="none" stroke="#eee" stroke-width="2"/></svg></div>
<h1 class="hero-title">Straight From The <span>Hive</span></h1>
<p class="hero-sub">DISCOVER THE NATURAL WONDERS OF MANUKA HONEY</p>
<a class="btn-pill solid">Shop Now</a>
<a class="btn-pill outline">Shop Now</a>

<section class="overview" role="img" aria-label="Faint honeycomb and bees backdrop in soft grey"></section>
<h2 class="section-title" style="left:110px;top:855px">Overview</h2>
<div class="divider-dots" style="left:108px;top:898px"><i></i><i></i></div>
<div class="divider" style="left:134px;top:903px;width:810px"></div>
<h3 class="overview-sub">An Introduction About Company</h3>
<p class="overview-text">Lorem Ipsum is simply dummy text of the printing and typesetting industry. Lorem Ipsum has been the industry's standard dummy text ever since the 1500s, when an unknown printer took a galley of type and scrambled it to make a type specimen book. It has survived not only five centuries, but also the leap into electronic typesetting, remaining essentially unchanged. It was popularised in the 1960s with the release of Typeline sheets containing Lorem Ipsum passages, and more recently with desktop publishing software like Pagecraft including versions of Lorem Ipsum.</p>
<a class="btn-block" style="left:102px;top:1129px;width:138px;height:38px">Know More</a>

<section class="products"></section>
<div class="products-card"></div>
<h2 class="section-title" style="left:92px;top:1346px">Our Products</h2>
<div class="divider-dots" style="left:90px;top:1389px"><i></i><i></i></div>
<div class="divider" style="left:124px;top:1394px;width:934px"></div>

<svg class="carousel-arrow" style="left:87px" width="48" height="18" viewBox="0 0 48 18"><path d="M47 9H2M10 1 2 9l8 8" fill="none" stroke="#222" stroke-width="1.6"/></svg>
<svg class="carousel-arrow" style="left:1069px" width="48" height="18" viewBox="0 0 48 18"><path d="M1 9h45M38 1l8 8-8 8" fill="none" stroke="#222" stroke-width="1.6"/></svg>

<div class="product" style="left:162px">
  <div class="product-photo" role="img" aria-label="Photo of a honey bowl with honeycomb and ginger" style="background:radial-gradient(circle at 50% 55%,#f0a82a 0%,#f6d58f 35%,#fff 70%)"></div>
  <span class="price">$9</span>
  <p class="product-name">Fitterarum formas</p>
  <p class="product-desc">Xom li tempor cum soluta nob is</p>
</div>
<div class="product" style="left:384px">
  <div class="product-photo" role="img" aria-label="Photo of a jar of honey with comb" style="background:radial-gradient(circle at 50% 55%,#f3bd3c 0%,#f8e0a0 35%,#fff 70%)"></div>
  <span class="price">$15</span>
  <p class="product-name">Fegentis in</p>
  <p class="product-desc">Ror cum soluta nob is eleifend</p>
</div>
<div class="product" style="left:607px">
  <div class="product-photo" role="img" aria-label="Photo of a honey jar beside honeycomb" style="background:radial-gradient(circle at 50% 60%,#e9a72b 0%,#f5d793 35%,#fff 70%)"></div>
  <span class="price">$16</span>
  <p class="product-name">Decima et quinta</p>
  <p class="product-desc">Empor cum soluta nob is eleifend</p>
</div>
<div class="product" style="left:831px">
  <div class="product-photo" role="img" aria-label="Photo of two tall jars of dark honey" style="background:radial-gradient(ellipse at 50% 55%,#b8461a 0%,#d88a4a 35%,#fff 70%)"></div>
  <span class="price">$3</span>
  <p class="product-name">Rigation quin</p>
  <p class="product-desc">Nam liber tear cum soluta nob is</p>
</div>

<a class="btn-dark">VIEW ALL PRODUCTS</a>

<section class="contact"></section>
<h2 class="section-title" style="left:100px;top:1940px">Contact Info</h2>
<div class="divider-dots" style="left:99px;top:1981px"><i style="background:#9a9a9a"></i><i style="background:#9a9a9a"></i></div>
<div class="divider" style="left:130px;top:1986px;width:924px;background:#555"></div>
<p class="contact-intro">Please fill this form to details and information about Exports and Whole Sale Inquiries.  Our  team  will revert you very soon.</p>

<svg class="abs" style="left:111px;top:2110px" width="18" height="24" viewBox="0 0 18 24"><path d="M9 1a7.5 7.5 0 0 0-7.5 7.5C1.5 14 9 23 9 23s7.5-9 7.5-14.5A7.5 7.5 0 0 0 9 1z" fill="#f0d000"/><circle cx="9" cy="8.5" r="2.8" fill="#333"/></svg>
<p class="contact-line" style="left:164px;top:2106px">64 Paddock Ln, Oakhurst,<br>Auckland 2469, New Zealand</p>

<p class="person-name" style="left:164px">Desmond Harlow<small>EXPORT MANAGER</small></p>
<p class="person-name" style="left:335px">Neil Forbes<small>MARKET INFORMATION</small></p>

<svg class="abs" style="left:108px;top:2224px" width="24" height="24" viewBox="0 0 24 24"><circle cx="12" cy="12" r="10.5" fill="none" stroke="#f0d000" stroke-width="2"/><path d="M8.5 7c-.8.5-1 1.6-.5 2.9 1 2.6 3.3 5 6 6.1 1.2.5 2.3.3 2.8-.5l-2-1.8-1.3.8c-1.2-.6-2.4-1.8-3-3l.8-1.3z" fill="#f0d000"/></svg>
<p class="contact-line" style="left:164px;top:2225px">+64 21 438 190</p>
<p class="contact-line" style="left:338px;top:2225px">+64 21 067 4183</p>

<svg class="abs" style="left:107px;top:2267px" width="24" height="17" viewBox="0 0 24 17"><rect x="1" y="1" width="22" height="15" fill="#f0d000"/><path d="M1 1l11 8 11-8" fill="none" stroke="#333" stroke-width="1.5"/></svg>
<p class="contact-line" style="left:164px;top:2264px">dkharlow@pelmail.co.nz</p>
<p class="contact-line" style="left:338px;top:2264px">tideflowernz@mailpost.com</p>

<div class="col-rule"></div>
<div class="form-badge">
  <svg width="30" height="30" viewBox="0 0 30 30" fill="none" stroke="#222" stroke-width="2"><rect x="5" y="4" width="16" height="22"/><path d="M9 10h8M9 15h8M9 20h4"/><path d="M26 9 17 21l-2 4 4-2 9-12z" fill="#f0d000"/></svg>
</div>

<div class="field" style="left:627px;top:2073px;width:476px">Name</div>
<div class="field" style="left:627px;top:2139px;width:217px">Phone</div>
<div class="field" style="left:865px;top:2139px;width:238px">Email</div>
<div class="field" style="left:627px;top:2236px;width:476px">Your Inquiry</div>
<a class="btn-submit">SUBMIT NOW</a>

<footer class="site-footer">
  <p class="copyright">© 2017 | Privacy policy</p>
  <div class="social"><i></i><i></i><i></i><i></i></div>
</footer>

</body>
</html>
```